Local fast-growing company in the service sector

We are looking for a modern business card design, which should also appear on our letterheads

Target Market(s)

Private and industrial sectors

Contact Information for Business Card

Vorname Name
Kellbacher Str. 38
74819 Waldbergen
Tel.: 07162-418395-0
Name@service-tkwl.de

Colors
9d9d9d
919191
aaaaaa

Requirements
Must have
• The logo (file) in silver

```html
<!DOCTYPE html>
<html lang="de">
<head>
<meta charset="utf-8">
<title>TKWL Visitenkarte</title>
<link href="https://fonts.googleapis.com/css2?family=Lato:wght@400;700&display=swap" rel="stylesheet">
<style>
  :root {
    --page: #d9d6d4;
    --card-light: #f1eeec;
    --card-mid: #e3dfdc;
    --silver: #9d9d9d;
    --silver-dark: #6e6e6e;
    --ink: #1f1f1f;
    --ink-soft: #3b3b3b;
    --band: #1e1e1e;
    --accent-line: #a08474;
    --icon-bg: #6a6664;
  }
  * { margin: 0; padding: 0; box-sizing: border-box; }
  html, body {
    width: 1200px; height: 970px; overflow: hidden;
    background: var(--page);
    font-family: "Lato", sans-serif;
  }
  .canvas { position: relative; width: 1200px; height: 970px; }
  .card {
    position: absolute; left: 100px; top: 185px;
    width: 1000px; height: 600px;
    background: linear-gradient(135deg, var(--card-light), var(--card-mid));
    border: 1px solid #ffffff;
    overflow: hidden;
  }
  .card__swoosh { position: absolute; left: 0; top: 0; width: 1000px; height: 600px; }
  .brand {
    position: absolute; left: 285px; top: 95px;
    display: flex; align-items: center; gap: 26px;
  }
  .brand__square { width: 92px; height: 92px; background: var(--silver); }
  .brand__name {
    font-weight: 700; font-size: 92px; line-height: 1;
    color: var(--silver-dark); letter-spacing: 2px;
  }
  .person {
    position: absolute; right: 610px; top: 338px; text-align: right;
  }
  .person__name { font-weight: 700; font-size: 28px; color: var(--ink-soft); }
  .person__role { font-size: 21px; color: var(--ink-soft); margin-top: 10px; }
  .divider {
    position: absolute; left: 449px; top: 281px; width: 3px; height: 172px;
    background: linear-gradient(to bottom, transparent, var(--silver-dark) 20%, var(--silver-dark) 80%, transparent);
  }
  .contact { position: absolute; left: 500px; top: 290px; color: var(--ink); }
  .contact__row {
    display: flex; align-items: center; gap: 17px;
    font-size: 23px; height: 34px; margin-bottom: 15px;
  }
  .contact__icon {
    width: 31px; height: 31px; border-radius: 50%;
    background: var(--icon-bg); display: flex; align-items: center; justify-content: center;
  }
  .contact__address { font-weight: 700; font-size: 22px; line-height: 33px; margin-top: 2px; }
</style>
</head>
<body>
<div class="canvas">
  <div class="card">
    <svg class="card__swoosh" viewBox="0 0 1000 600" aria-hidden="true">
      <path d="M0 600 L0 578 L210 578 C560 575 820 540 1000 470 L1000 600 Z" fill="var(--band)"/>
      <path d="M215 563 C560 560 820 520 1000 455" fill="none" stroke="var(--accent-line)" stroke-width="3"/>
    </svg>

    <div class="brand">
      <div class="brand__square"></div>
      <div class="brand__name">TKWL</div>
    </div>

    <div class="person">
      <div class="person__name">Miriam Hollander</div>
      <div class="person__role">Vendra Advisors</div>
    </div>

    <div class="divider"></div>

    <div class="contact">
      <div class="contact__row">
        <span class="contact__icon">
          <svg width="18" height="18" viewBox="0 0 24 24"><path d="M6.6 10.8a15 15 0 0 0 6.6 6.6l2.2-2.2c.3-.3.7-.4 1-.2 1.1.4 2.3.6 3.6.6.6 0 1 .4 1 1V20c0 .6-.4 1-1 1A17 17 0 0 1 3 4c0-.6.4-1 1-1h3.5c.6 0 1 .4 1 1 0 1.3.2 2.5.6 3.6.1.3 0 .7-.2 1z" fill="#f1eeec"/></svg>
        </span>
        <span>07162-418395-0</span>
      </div>
      <div class="contact__row">
        <span class="contact__icon">
          <svg width="17" height="17" viewBox="0 0 24 24"><rect x="3" y="5" width="18" height="14" rx="1" fill="none" stroke="#f1eeec" stroke-width="2"/><path d="M3 6l9 7 9-7" fill="none" stroke="#f1eeec" stroke-width="2"/></svg>
        </span>
        <span>mhollander@service-tkwl.de</span>
      </div>
      <div class="contact__address">
        Kellbacher Str. 38<br>74819 Waldbergen
      </div>
    </div>
  </div>
</div>
</body>
</html>
```